SUMMIT GATHERING 2021. August 20th -22nd.

The Hosts of the conference: Grace Tabernacle-Pastors Ron n Molly ( Picture with two persons)

Guest Minister: Bishop Lorna Kiprotich. (Cedar Ridge Evangelist)

Venue:
Seattle Harborgate Lodge. 4817 North 92nd Avenue Seattle, WA 98134.

Conference times.
Friday August 20th 6pm-8:30pm
Saturday August 21st. 6pm-8:30pm

Sunday August 22nd 10am-1pm
“ CHURCH RENEWAL SERVICE”

5pm-7:30pm
TWOFOLD BLESSING SERVICE.

Target Market(s)

18-55

Industry/Entity Type

Religious/ Entertainment.

Requirements
Must have
• A highlight of the Relaunch service on Sunday August 22nd 5pm-7:30pm.
Nice to have
• Excellent ideas….

```html
<!DOCTYPE html>
<html lang="en">
<head>
<meta charset="UTF-8">
<title>Summit Gathering 2021</title>
<link href="https://fonts.googleapis.com/css2?family=Montserrat:wght@400;700;800;900&family=Oswald:wght@300;400;500&family=Parisienne&display=swap" rel="stylesheet">
<style>
  :root {
    --backdrop: #d9d9d7;
    --poster-dark: #10151c;
    --poster-mid: #1c2430;
    --gold: #e0a93a;
    --gold-light: #f6cf6a;
    --gold-deep: #b77b1c;
    --white: #ffffff;
    --silver: #cfd6de;
    --steel-blue: #7fa2c0;
    --ink: #1a1a1a;
  }
  * { margin: 0; padding: 0; box-sizing: border-box; }
  html, body { width: 1200px; height: 800px; overflow: hidden; background: var(--backdrop); }
  .canvas { position: relative; width: 1200px; height: 800px; }
  .poster {
    position: absolute; left: 333px; top: 25px; width: 534px; height: 750px; overflow: hidden;
    background: radial-gradient(ellipse at 60% 35%, var(--poster-mid) 0%, var(--poster-dark) 70%);
    font-family: 'Montserrat', sans-serif; color: var(--white);
  }
  .ornament-top {
    position: absolute; left: 57px; top: 0; width: 477px; height: 85px;
    background: radial-gradient(ellipse at 55% 0%, rgba(224,169,58,0.35) 0%, rgba(224,169,58,0.08) 45%, rgba(16,21,28,0) 75%);
  }
  .ornament-bottom {
    position: absolute; left: 297px; top: 575px; width: 237px; height: 175px;
    background: radial-gradient(ellipse at 85% 90%, rgba(224,169,58,0.30) 0%, rgba(11,15,21,0.9) 55%, rgba(16,21,28,0) 80%);
  }
  .title-script {
    position: absolute; left: 52px; top: 10px; font-family: 'Parisienne', cursive;
    font-size: 78px; color: var(--gold); letter-spacing: 4px; line-height: 1;
  }
  .title-main {
    position: absolute; left: 40px; top: 86px; font-family: 'Montserrat', sans-serif; font-weight: 900;
    font-size: 54px; letter-spacing: 0.5px; line-height: 1;
    color: var(--silver); text-shadow: 2px 3px 0 #5d7896;
  }
  .event-date { position: absolute; left: 197px; top: 152px; font-weight: 700; font-size: 15px; }
  .event-year {
    position: absolute; left: 377px; top: 136px; font-family: 'Oswald', sans-serif; font-weight: 300;
    font-size: 74px; color: var(--steel-blue); line-height: 1;
    transform: scaleX(0.86); transform-origin: left top;
  }
  .hosts-photo {
    position: absolute; left: 24px; top: 213px; width: 181px; height: 225px; border-radius: 14px;
    border: 2px solid var(--gold);
    background: linear-gradient(160deg, #4b3a33 0%, #d9d2cc 45%, #2b2523 100%);
  }
  .guest-photo {
    position: absolute; left: 257px; top: 210px; width: 148px; height: 148px; border-radius: 50%;
    border: 4px solid var(--gold);
    background: radial-gradient(circle at 50% 40%, #6a4b3c 0%, #b9b3ad 60%, #e6e3df 100%);
  }
  .label {
    position: absolute; font-family: 'Montserrat', sans-serif; font-weight: 800; font-size: 7px;
    letter-spacing: 4.5px; text-transform: uppercase; color: var(--white);
  }
  .hosts-label { left: 40px; top: 472px; }
  .hosts-names { position: absolute; left: 40px; top: 488px; font-weight: 700; font-size: 11.5px; line-height: 15px; }
  .guest-label { left: 288px; top: 391px; }
  .guest-name {
    position: absolute; left: 287px; top: 403px; font-family: 'Oswald', sans-serif; font-size: 16px;
    line-height: 25px; text-transform: uppercase;
  }
  .venue-pin { position: absolute; left: 262px; top: 473px; width: 12px; height: 16px; }
  .venue-label { left: 288px; top: 478px; }
  .venue-address {
    position: absolute; left: 287px; top: 503px; font-family: 'Oswald', sans-serif; font-size: 16px;
    line-height: 24px; text-transform: uppercase; width: 230px;
  }
  .times-label { left: 40px; top: 553px; }
  .schedule {
    position: absolute; left: 40px; font-family: 'Oswald', sans-serif; font-size: 14px; line-height: 21px;
    text-transform: uppercase;
  }
  .schedule .time { font-weight: 300; }
  .schedule-weeknights { top: 570px; }
  .highlight-band {
    position: absolute; left: 0; top: 617px; width: 310px; height: 63px;
    background: linear-gradient(90deg, var(--gold-deep) 0%, var(--gold-light) 55%, var(--gold) 100%);
  }
  .schedule-sunday { top: 630px; color: var(--ink); font-weight: 500; }
  .schedule-evening { top: 686px; }
</style>
</head>
<body>
<main class="canvas">
  <article class="poster">
    <div class="ornament-top" role="img" aria-label="Gold swirl ornament"></div>
    <div class="ornament-bottom" role="img" aria-label="Gold and black swirl ornament"></div>

    <div class="title-script">summit</div>
    <h1 class="title-main">GATHERING</h1>
    <p class="event-date">August 20th -22nd</p>
    <p class="event-year">2021</p>

    <div class="hosts-photo" role="img" aria-label="Photo of the hosts, Pastors Ron and Molly"></div>
    <div class="guest-photo" role="img" aria-label="Portrait of guest minister Bishop Lorna Kiprotich"></div>

    <p class="label guest-label">Guest Minister</p>
    <p class="guest-name">Bishop Lorna Kiprotich<br>(Cedar Ridge Evangelist)</p>

    <p class="label hosts-label">Hosts</p>
    <p class="hosts-names">Grace Tabernacle-Pastors<br>Ron n Molly</p>

    <svg class="venue-pin" viewBox="0 0 12 16" aria-hidden="true">
      <path d="M6 0 C2.7 0 0 2.6 0 5.8 C0 10 6 16 6 16 C6 16 12 10 12 5.8 C12 2.6 9.3 0 6 0 Z" fill="var(--gold)"/>
      <circle cx="6" cy="5.8" r="2.2" fill="var(--poster-dark)"/>
    </svg>
    <p class="label venue-label">Venue</p>
    <p class="venue-address">Seattle Harborgate Lodge. 4817 North 92nd Avenue Seattle, WA 98134.</p>

    <p class="label times-label">Conference Times</p>
    <p class="schedule schedule-weeknights">
      Friday August 20th <span class="time">6PM-8:30PM</span><br>
      Saturday August 21st. <span class="time">6PM-8:30PM</span>
    </p>

    <div class="highlight-band"></div>
    <p class="schedule schedule-sunday">
      Sunday August 22nd <span class="time">10AM-1PM</span><br>
      “ Church Renewal Service”
    </p>

    <p class="schedule schedule-evening">
      <span class="time">5PM-7:30PM</span><br>
      Twofold Blessing Service
    </p>
  </article>
</main>
</body>
</html>
```